Company service wheel graphic

A graphic demonstrating all the services the company offers.
I have hand drawn and written up on the attached the content that is required. Also attached is our company logo so you have a sense of the colour scheme of the logo.
This will eventually go into a company brochure, be used on our website etc.

Target Market(s)

Local GOvernment and other professionals who work in the sport, recreation and leisure industries

Industry/Entity Type

Sports, recreation, leisure, aquatics

Font styles to use
Other font styles liked:
• Calibri

Colors
0054AA
0677BA
7BADD7
CADEEF
E8F1F8

Requirements
Must have
• An eye catching graphic that captures all the information in the hand drawn atachement.
Nice to have
• Each quadrant in the circle to have its own colour, that links to the company logo

```html
<!DOCTYPE html>
<html lang="en">
<head>
<meta charset="utf-8">
<title>Service Wheel</title>
<link href="https://fonts.googleapis.com/css2?family=Carlito:wght@400;700&display=swap" rel="stylesheet">
<style>
  :root {
    --ink-ring: #1a5fa8;
    --rim: #a9dcf0;
    --blue: #0f72ba;
    --orange: #f05a28;
    --green: #05673a;
    --plum: #9b1b5e;
    --magenta: #e5097f;
    --cyan: #00aeef;
    --plum-inner: #8e1a57;
    --blue-inner: #1a74bc;
    --white: #ffffff;
  }
  html, body {
    margin: 0;
    padding: 0;
    width: 1200px;
    height: 1200px;
    overflow: hidden;
    background: var(--white);
  }
  .service-wheel {
    display: block;
    width: 1200px;
    height: 1200px;
    font-family: "Carlito", "Calibri", sans-serif;
  }
  .rim { fill: none; stroke: var(--rim); stroke-width: 2; }
  .q-blue { fill: var(--blue); }
  .q-orange { fill: var(--orange); }
  .q-green { fill: var(--green); }
  .q-plum { fill: var(--plum); }
  .band-top { fill: var(--magenta); }
  .band-bottom { fill: var(--cyan); }
  .core-planning { fill: var(--plum-inner); }
  .core-management { fill: var(--green); }
  .core-participation { fill: var(--orange); }
  .core-impact { fill: var(--blue-inner); }
  .hub { fill: var(--cyan); stroke: var(--white); stroke-width: 2; }
  .audience {
    fill: var(--ink-ring);
    font-size: 30px;
    letter-spacing: 1.5px;
  }
  .band-label {
    fill: var(--white);
    font-weight: 700;
    font-size: 24px;
  }
  .pillar-label {
    fill: var(--white);
    font-size: 21px;
  }
  .hub-label {
    fill: var(--white);
    font-weight: 700;
    font-size: 21px;
    text-anchor: middle;
  }
  .service { fill: var(--white); font-size: 21.5px; }
  .bullet { fill: var(--white); }
</style>
</head>
<body>
<svg class="service-wheel" viewBox="0 0 1040 1040" xmlns="http://www.w3.org/2000/svg" role="img" aria-label="Service wheel showing planning, management, participation and community impact services">
  <defs>
    <path id="arc-audience-top" d="M52,520 A468,468 0 0 1 988,520"/>
    <path id="arc-audience-bottom" d="M22,520 A498,498 0 0 0 1018,520"/>
    <path id="arc-band-top" d="M326,540 A194,194 0 1 1 714,540"/>
    <path id="arc-band-bottom" d="M313,520 A207,207 0 0 0 727,520"/>
    <path id="arc-core-top" d="M372,520 A148,148 0 0 1 668,520"/>
    <path id="arc-core-inner" d="M392,520 A128,128 0 0 0 648,520"/>
    <path id="arc-core-outer" d="M368,520 A152,152 0 0 0 672,520"/>
  </defs>

  <!-- outer rim -->
  <circle class="rim" cx="520" cy="520" r="510"/>

  <!-- audience labels -->
  <text class="audience"><textPath href="#arc-audience-top" startOffset="31%" text-anchor="middle">LOCAL + STATE GOVERNMENT</textPath></text>
  <text class="audience"><textPath href="#arc-audience-top" startOffset="69%" text-anchor="middle">SPORT + LEISURE FACILITY MANAGERS</textPath></text>
  <text class="audience"><textPath href="#arc-audience-bottom" startOffset="27%" text-anchor="middle">INVESTORS, DEVELOPERS, ARCHITECTS + DESIGNERS</textPath></text>
  <text class="audience"><textPath href="#arc-audience-bottom" startOffset="75%" text-anchor="middle">SPORT, RECREATION + COMMUNITY PROVIDERS</textPath></text>

  <!-- quadrants -->
  <path class="q-blue" d="M520,520 L65,520 A455,455 0 0 1 520,65 Z"/>
  <path class="q-orange" d="M520,520 L520,65 A455,455 0 0 1 975,520 Z"/>
  <path class="q-green" d="M520,520 L65,520 A455,455 0 0 0 520,975 Z"/>
  <path class="q-plum" d="M520,520 L520,975 A455,455 0 0 0 975,520 Z"/>

  <!-- middle band -->
  <path class="band-top" d="M308,520 A212,212 0 0 1 732,520 Z"/>
  <path class="band-bottom" d="M308,520 A212,212 0 0 0 732,520 Z"/>
  <text class="band-label"><textPath href="#arc-band-top" startOffset="50%" text-anchor="middle">Community, Aquatic + Recreation Facilities</textPath></text>
  <text class="band-label"><textPath href="#arc-band-bottom" startOffset="50%" text-anchor="middle">Community Activation</textPath></text>

  <!-- core pillars -->
  <path class="core-planning" d="M520,520 L344,520 A176,176 0 0 1 520,344 Z"/>
  <path class="core-management" d="M520,520 L520,344 A176,176 0 0 1 696,520 Z"/>
  <path class="core-participation" d="M520,520 L344,520 A176,176 0 0 0 520,696 Z"/>
  <path class="core-impact" d="M520,520 L520,696 A176,176 0 0 0 696,520 Z"/>

  <text class="pillar-label"><textPath href="#arc-core-top" startOffset="25%" text-anchor="middle">Planning</textPath></text>
  <text class="pillar-label"><textPath href="#arc-core-top" startOffset="75%" text-anchor="middle">Management</textPath></text>
  <text class="pillar-label"><textPath href="#arc-core-inner" startOffset="25%" text-anchor="middle">Growing</textPath></text>
  <text class="pillar-label"><textPath href="#arc-core-outer" startOffset="25%" text-anchor="middle">Participation</textPath></text>
  <text class="pillar-label"><textPath href="#arc-core-inner" startOffset="75%" text-anchor="middle">Community</textPath></text>
  <text class="pillar-label"><textPath href="#arc-core-outer" startOffset="75%" text-anchor="middle">Impact + Outcomes</textPath></text>

  <!-- hub -->
  <circle class="hub" cx="520" cy="520" r="97"/>
  <text class="hub-label" x="520" y="477">Community</text>
  <text class="hub-label" x="520" y="503">+</text>
  <text class="hub-label" x="520" y="536">Stakeholder</text>
  <text class="hub-label" x="520" y="566">Engagement</text>

  <!-- planning services -->
  <g class="service-list planning-services">
    <polygon class="bullet" points="282,160 295,167 282,174"/>
    <text class="service" x="310" y="175">Feacibility Studies</text>
    <polygon class="bullet" points="222,200 235,207 222,214"/>
    <text class="service" x="248" y="215">Community +</text>
    <text class="service" x="248" y="245">Stakeholder Research</text>
    <polygon class="bullet" points="166,273 179,280 166,287"/>
    <text class="service" x="193" y="288">Sport + Recreation Strategies</text>
    <polygon class="bullet" points="130,322 143,329 130,336"/>
    <text class="service" x="156" y="337">Design Strategies</text>
    <polygon class="bullet" points="112,370 125,377 112,384"/>
    <text class="service" x="138" y="385">Indoor +</text>
    <text class="service" x="138" y="415">Outdoor Spaces</text>
  </g>

  <!-- management services -->
  <g class="service-list management-services">
    <polygon class="bullet" points="535,125 548,132 535,139"/>
    <text class="service" x="562" y="140">Activating</text>
    <text class="service" x="562" y="170">Underutilised Assets</text>
    <polygon class="bullet" points="535,193 548,200 535,207"/>
    <text class="service" x="564" y="208">Income + Revenue</text>
    <text class="service" x="564" y="238">Generation Strategies</text>
    <polygon class="bullet" points="535,263 548,270 535,277"/>
    <text class="service" x="568" y="278">Mystery Shopper + Business</text>
    <text class="service" x="568" y="308">Health Checks</text>
    <polygon class="bullet" points="707,336 720,343 707,350"/>
    <text class="service" x="735" y="351">Financial +</text>
    <text class="service" x="735" y="381">Funding strategies</text>
    <polygon class="bullet" points="739,406 752,413 739,420"/>
    <text class="service" x="768" y="421">Management</text>
    <text class="service" x="768" y="451">Support</text>
    <polygon class="bullet" points="749,476 762,483 749,490"/>
    <text class="service" x="776" y="491">Business Planning</text>
  </g>

  <!-- participation services -->
  <g class="service-list participation-services">
    <polygon class="bullet" points="88,547 101,554 88,561"/>
    <text class="service" x="116" y="562">Trends + Insights</text>
    <polygon class="bullet" points="98,590 111,597 98,604"/>
    <text class="service" x="128" y="605">Health Profiling</text>
    <polygon class="bullet" points="112,631 125,638 112,645"/>
    <text class="service" x="142" y="646">Active Recreation</text>
    <text class="service" x="142" y="676">Strategies</text>
    <polygon class="bullet" points="138,701 151,708 138,715"/>
    <text class="service" x="168" y="716">Community</text>
    <text class="service" x="168" y="746">Program Development</text>
    <polygon class="bullet" points="188,774 201,781 188,788"/>
    <text class="service" x="217" y="789">Physical Activity Strategies</text>
    <polygon class="bullet" points="212,814 225,821 212,828"/>
    <text class="service" x="240" y="829">Specific Cohort Strategies</text>
    <polygon class="bullet" points="258,856 271,863 258,870"/>
    <text class="service" x="286" y="871">Sports + Program</text>
    <text class="service" x="308" y="901">Specific Strategies</text>
  </g>

  <!-- impact services -->
  <g class="service-list impact-services">
    <polygon class="bullet" points="732,591 745,598 732,605"/>
    <text class="service" x="757" y="606">Community</text>
    <text class="service" x="757" y="636">Impact Monitoring</text>
    <polygon class="bullet" points="706,665 719,672 706,679"/>
    <text class="service" x="733" y="680">Social Value</text>
    <polygon class="bullet" points="626,723 639,730 626,737"/>
    <text class="service" x="652" y="738">Community Outcomes +</text>
    <text class="service" x="652" y="768">KPIs</text>
    <polygon class="bullet" points="556,797 569,804 556,811"/>
    <text class="service" x="584" y="812">Contract Monitoring</text>
  </g>
</svg>
</body>
</html>
```